The Brambury Firm

We need a new design for our letterhead and envelopes. We are a personal injury and criminal defense firm so we need something modern and clean, but more on the professional/traditional side. Our new logo has two colors and is attached to the file so we need something that works well with those colors/matches the design. The following information needs to be on the letterhead:
Phone: (555) 314-7265
Fax: (555) 419-6032
Toll-Free: (555) 736-1149
Post Office Box 4273
Tallowmere, TQ 29458-4273
TQHarmClaimsDesk.example
PalmettoShieldCounsel.example

Target Market(s)

Clients, government agencies, other law firms

Industry/Entity Type

Legal

Font styles to use
Sans Serif
Other font styles liked:
• Arial

Colors

Designer to choose colors to be used in the design.

Requirements
Must have
• Must look professional and clean, modern
Nice to have
• I would like to see a design that works with the logo but does not distract from the content that will be printed on it
Should not have
• Too many colors or crazy designs.

```html
<!DOCTYPE html>
<html lang="en">
<head>
<meta charset="utf-8">
<title>The Brambury Firm – Stationery</title>
<link href="https://fonts.googleapis.com/css2?family=Arimo:wght@400;700&display=swap" rel="stylesheet">
<style>
  :root {
    --navy: #2e3190;
    --red: #d7262b;
    --ink: #1a1a1a;
    --paper: #ffffff;
    --backdrop: #e6e7e9;
    --shadow: 0 8px 22px rgba(0,0,0,0.16);
  }
  * { box-sizing: border-box; margin: 0; padding: 0; }
  html, body { width: 1200px; height: 1200px; overflow: hidden; }
  body {
    background: var(--backdrop);
    font-family: "Arimo", Arial, sans-serif;
    color: var(--ink);
    position: relative;
  }
  .sheet { position: absolute; background: var(--paper); box-shadow: var(--shadow); }

  /* brand name lockup */
  .brand { display: flex; align-items: center; gap: 8px; }
  .brand-dot { width: 14px; height: 14px; border-radius: 50%; background: var(--red); flex: none; }
  .brand-name {
    font-family: "Arimo", Arial, sans-serif;
    font-weight: 700;
    color: var(--navy);
    text-transform: uppercase;
    letter-spacing: 0.04em;
    white-space: nowrap;
  }

  /* letterhead */
  .letterhead { left: 60px; top: 200px; width: 520px; height: 736px; padding: 70px 70px 0 80px; }
  .letterhead .brand-name { font-size: 19px; }
  .salutation { margin-top: 90px; font-size: 9px; font-weight: 700; }
  .letter-body { margin-top: 22px; font-size: 8.2px; line-height: 1.5; }
  .letter-body p + p { margin-top: 12px; }
  .sign-off { display: flex; margin-top: 40px; font-size: 7.5px; gap: 80px; align-items: flex-end; }
  .sign-off .name { font-weight: 700; }
  .sign-off .label { font-weight: 700; display: flex; align-items: flex-end; gap: 14px; }
  .signature-mark { width: 70px; height: 40px; background: linear-gradient(#fff, #f2f2f2); border-bottom: 1px solid #222; }
  .contact-block { display: flex; gap: 48px; font-size: 7.2px; line-height: 1.45; }
  .letterhead .contact-block { position: absolute; left: 80px; bottom: 70px; }
  .contact-block .gap { margin-top: 10px; }

  /* folder */
  .folder {
    left: 640px; top: 50px; width: 500px; height: 540px;
    background: var(--navy);
    display: flex; align-items: center; justify-content: center;
  }
  .folder .brand-name { color: var(--paper); font-size: 30px; }
  .folder .brand-dot { width: 26px; height: 26px; }

  /* envelope front */
  .envelope-front {
    left: 640px; top: 630px; width: 500px; height: 240px;
    display: flex; align-items: center; justify-content: center;
  }
  .envelope-front .brand-name { font-size: 26px; }
  .envelope-front .brand-dot { width: 22px; height: 22px; }

  /* envelope back */
  .envelope-back { left: 620px; top: 910px; width: 520px; height: 250px; overflow: hidden; }
  .envelope-flap { position: absolute; left: 0; top: 0; width: 100%; height: 56px; }
  .envelope-back .brand { position: absolute; left: 40px; top: 150px; }
  .envelope-back .brand-name { font-size: 15px; }
  .envelope-back .contact-block { position: absolute; left: 250px; top: 150px; gap: 28px; font-size: 7px; }
</style>
</head>
<body>

  <section class="sheet letterhead" aria-label="Letterhead">
    <div class="brand"><span class="brand-dot"></span><span class="brand-name">The Brambury Firm</span></div>
    <p class="salutation">Dear Mr. John DOE</p>
    <div class="letter-body">
      <p>Locavore cornhole air plant, prism before they sold out succulents ethical pop-up letterpress unicorn health goth tousled selvage XOXO. Wolf lyft 90's, franzen tousled man bun palo santo helvetica shabby chic mixtape. Lumbersexual 8-bit gastropub tilde, af tbh selfies glossier master cleanse letterpress church-key. Farm-to-table subway tile unicorn waistcoat vape venmo bespoke wolf celiac mustache small batch cliche fam. Small batch craft beer cred slow-carb polaroid irony banh mi thundercats waistcoat. Distillery forage put a bird on it pabst.</p>
      <p>Swag viral occupy ennui, marfa next level lyft cred. Distillery thundercats leggings, shoreditch unicorn chambray vexillologist migas af etsy listicle salvia XOXO. Asymmetrical selvage you probably haven't heard of them church-key literally biodiesel. Chillwave poutine bitters freegan kitsch. Cold-pressed copper mug vice chicharrones edison bulb +1 snackwave hot chicken mustache sriracha whatever tumeric. Heirloom umami man braid chicharrones shaman retro.</p>
      <p>Church-key four loko ramps man bun, irony mlkshk meggings gastropub tacos. Flannel fanny pack kitsch whatever brooklyn. Hell of gastropub succulents single-origin coffee sriracha. +1 palo santo fam synth sustainable you probably haven't heard of them, hoodie brunch mumblecore narwhal street art iPhone selfies bicycle rights man braid. Four loko gastropub celiac, tousled venmo slow-carb helvetica pok pok.</p>
    </div>
    <div class="sign-off">
      <div><div class="name">Name &amp; Surname</div><div>Position</div></div>
      <div class="label">Signature: <span class="signature-mark" role="img" aria-label="Handwritten signature"></span></div>
    </div>
    <div class="contact-block">
      <div>
        <div>P: (555) 314-7265</div>
        <div>F: (555) 419-6032</div>
        <div class="gap">Toll-Free: (555) 736-1149</div>
      </div>
      <div>
        <div>Post Office Box 4273</div>
        <div>Tallowmere, TQ 29458-4273</div>
        <div class="gap">www.TQHarmClaimsDesk.example</div>
        <div>www.PalmettoShieldCounsel.example</div>
      </div>
    </div>
  </section>

  <section class="sheet folder" aria-label="Presentation folder">
    <div class="brand"><span class="brand-dot"></span><span class="brand-name">The Brambury Firm</span></div>
  </section>

  <section class="sheet envelope-front" aria-label="Envelope front">
    <div class="brand"><span class="brand-dot"></span><span class="brand-name">The Brambury Firm</span></div>
  </section>

  <section class="sheet envelope-back" aria-label="Envelope back">
    <svg class="envelope-flap" viewBox="0 0 520 56" preserveAspectRatio="none" aria-hidden="true">
      <polygon points="0,0 520,0 490,56 22,56" fill="var(--navy)"/>
    </svg>
    <div class="brand"><span class="brand-dot"></span><span class="brand-name">The Brambury Firm</span></div>
    <div class="contact-block">
      <div>
        <div>P: (555) 314-7265</div>
        <div>F: (555) 419-6032</div>
        <div class="gap">T-F: (555) 736-1149</div>
      </div>
      <div>
        <div>Post Office Box 4273</div>
        <div>Tallowmere, TQ 29458-4273</div>
        <div class="gap">www.TQHarmClaimsDesk.example</div>
        <div>www.PalmettoShieldCounsel.example</div>
      </div>
    </div>
  </section>

</body>
</html>
```